Plastic surgery office stationary
Larkmere cosmetic surgical group and dr's name is tomas ellingwarde
Plastic surgery office stationary - Medical
Creative Brief
Simple
Larkmere cosmetic surgical group
dr tomas ellingwarde
4172 Corvell blvd suite 3050 Beverly Hills, ca 90214
866 GLO VIDA (866.456.8432)
drtomas@glovidaclinic.com
www.GloVidaClinic.com

```html
<!DOCTYPE html>
<html lang="en">
<head>
<meta charset="utf-8">
<title>Larkmere Cosmetic Surgical Group – Stationery</title>
<link href="https://fonts.googleapis.com/css2?family=Lato:wght@400;700&display=swap" rel="stylesheet">
<style>
:root{
  --bg-light:#f3c6e2;
  --bg-mid:#e7a0cc;
  --bg-dark:#c9559c;
  --magenta:#b0126f;
  --magenta-deep:#8a0b56;
  --pink-soft:#e98bc2;
  --paper:#ffffff;
  --ink:#7a2457;
  --grey:#9a8a94;
}
*{margin:0;padding:0;box-sizing:border-box}
html,body{width:1200px;height:269px;overflow:hidden}
body{font-family:"Lato",sans-serif;color:var(--ink);
  background:linear-gradient(90deg,var(--bg-mid) 0%,var(--bg-light) 12%,var(--bg-light) 23%,var(--bg-dark) 24%,var(--bg-mid) 60%,var(--bg-dark) 100%)}
.canvas{position:relative;width:1200px;height:269px}
.item{position:absolute;overflow:hidden;box-shadow:0 1px 3px rgba(90,0,50,.35)}
.paper{background:var(--paper)}
.ink{background:linear-gradient(135deg,var(--magenta) 0%,var(--magenta-deep) 100%)}
.wave{position:absolute;left:0;width:100%}
.brand{position:absolute;display:flex;align-items:center;gap:2px;font-weight:700;color:var(--magenta);white-space:nowrap}
.brand .dot{border-radius:50%;background:currentColor}
.ink .brand{color:var(--paper)}
.contact{position:absolute;font-size:2.2px;line-height:3px;color:var(--grey);white-space:nowrap}
.lines i{display:block;height:1.3px;background:#e4dbe0;margin-bottom:2.4px}
.fax-title{position:absolute;font-size:12px;color:#555}
.fax-field{font-size:3px;color:#777;display:flex;gap:4px;margin-bottom:3px}
.disc{position:absolute;border-radius:50%}
</style>
</head>
<body>
<div class="canvas">

  <!-- business cards -->
  <div class="item ink" style="left:7px;top:115px;width:44px;height:25px">
    <div class="brand" style="left:8px;top:9px;font-size:5px"><span class="dot" style="width:3px;height:3px"></span>Larkmere</div>
  </div>
  <div class="item paper" style="left:7px;top:148px;width:44px;height:25px">
    <svg class="wave" style="bottom:0" viewBox="0 0 44 10" height="10" preserveAspectRatio="none"><path d="M0 6 Q22 0 44 4 V10 H0Z" fill="var(--magenta)"/></svg>
    <div class="contact" style="left:3px;top:3px;font-size:2px;line-height:2.6px">Consultations by appointment<br>Call the front desk<br>Aftercare support available</div>
  </div>

  <!-- letterhead -->
  <div class="item paper" style="left:53px;top:43px;width:96px;height:159px">
    <div class="brand" style="left:8px;top:10px;font-size:7px"><span class="dot" style="width:4px;height:4px"></span>Larkmere</div>
    <div class="lines" style="position:absolute;left:8px;top:40px;width:78px"><i></i><i></i><i></i><i></i><i></i><i></i><i></i><i style="width:60%"></i></div>
    <svg class="wave" style="bottom:0" viewBox="0 0 96 30" height="30" preserveAspectRatio="none"><path d="M0 16 Q50 2 96 12 V30 H0Z" fill="var(--pink-soft)"/><path d="M0 22 Q50 8 96 18 V30 H0Z" fill="var(--magenta)"/></svg>
    <div class="contact" style="left:8px;bottom:3px;color:#fff">Consultations by appointment only · Contact our front desk</div>
  </div>

  <!-- envelopes -->
  <div class="item paper" style="left:156px;top:116px;width:50px;height:28px">
    <div class="brand" style="left:4px;top:4px;font-size:4px"><span class="dot" style="width:2.5px;height:2.5px"></span>Larkmere</div>
    <svg class="wave" style="bottom:0" viewBox="0 0 50 8" height="8" preserveAspectRatio="none"><path d="M0 5 Q25 0 50 3 V8 H0Z" fill="var(--magenta)"/></svg>
  </div>
  <div class="item ink" style="left:156px;top:150px;width:50px;height:28px">
    <svg viewBox="0 0 50 28" width="50" height="28"><path d="M0 0 L25 14 L50 0" fill="none" stroke="rgba(255,255,255,.35)" stroke-width=".6"/></svg>
  </div>

  <!-- compliment slip -->
  <div class="item paper" style="left:210px;top:108px;width:13px;height:22px">
    <svg class="wave" style="bottom:0" viewBox="0 0 13 6" height="6" preserveAspectRatio="none"><path d="M0 3 Q6 0 13 2 V6 H0Z" fill="var(--magenta)"/></svg>
  </div>

  <!-- appointment cards -->
  <div class="item paper" style="left:234px;top:128px;width:48px;height:22px">
    <div class="brand" style="left:4px;top:4px;font-size:4px"><span class="dot" style="width:2.5px;height:2.5px"></span>Larkmere</div>
    <svg class="wave" style="bottom:0" viewBox="0 0 48 7" height="7" preserveAspectRatio="none"><path d="M0 5 Q24 0 48 3 V7 H0Z" fill="var(--magenta)"/></svg>
  </div>
  <div class="item ink" style="left:234px;top:156px;width:48px;height:24px"></div>

  <!-- presentation folder cover -->
  <div class="item paper" style="left:290px;top:20px;width:104px;height:225px">
    <svg class="wave" style="top:0" viewBox="0 0 104 60" height="60" preserveAspectRatio="none"><path d="M0 0 H104 V30 Q50 60 0 40Z" fill="var(--magenta)"/></svg>
    <div class="brand" style="left:0;right:0;top:100px;font-size:10px;flex-direction:column;gap:3px"><span class="dot" style="width:10px;height:10px"></span>Larkmere</div>
    <svg class="wave" style="bottom:0" viewBox="0 0 104 50" height="50" preserveAspectRatio="none"><path d="M0 20 Q60 0 104 18 V50 H0Z" fill="var(--pink-soft)"/><path d="M0 30 Q60 10 104 28 V50 H0Z" fill="var(--magenta)"/></svg>
  </div>

  <!-- open folder -->
  <div class="item ink" style="left:396px;top:20px;width:108px;height:225px">
    <svg viewBox="0 0 108 225" width="108" height="225"><path d="M0 130 Q54 110 108 130 V225 H0Z" fill="var(--pink-soft)"/><path d="M0 140 Q54 120 108 140" fill="none" stroke="#fff" stroke-width=".8" opacity=".6"/><rect x="40" y="165" width="28" height="16" fill="none" stroke="#fff" stroke-width=".6" opacity=".7"/></svg>
  </div>

  <!-- CD -->
  <div class="disc" style="left:540px;top:84px;width:48px;height:48px;background:radial-gradient(circle,var(--bg-light) 0 12%,var(--paper) 13% 40%,var(--magenta) 41% 100%);box-shadow:0 1px 3px rgba(90,0,50,.35)"></div>

  <!-- small card -->
  <div class="item paper" style="left:530px;top:190px;width:58px;height:28px">
    <div class="brand" style="left:5px;top:5px;font-size:4px"><span class="dot" style="width:2.5px;height:2.5px"></span>Larkmere</div>
    <svg class="wave" style="bottom:0" viewBox="0 0 58 8" height="8" preserveAspectRatio="none"><path d="M0 5 Q29 0 58 3 V8 H0Z" fill="var(--magenta)"/></svg>
  </div>

  <!-- fax sheet -->
  <div class="item paper" style="left:600px;top:48px;width:96px;height:180px">
    <div class="fax-title" style="left:8px;top:8px">Fax</div>
    <div style="position:absolute;left:8px;top:30px">
      <div class="fax-field"><span>To</span><span>From</span></div>
      <div class="fax-field"><span>Date</span><span>Pages</span></div>
    </div>
    <div class="lines" style="position:absolute;left:8px;top:50px;width:78px"><i></i><i></i><i></i><i></i><i></i></div>
    <svg class="wave" style="bottom:0" viewBox="0 0 96 20" height="20" preserveAspectRatio="none"><path d="M0 12 Q50 2 96 10 V20 H0Z" fill="var(--magenta)"/></svg>
  </div>

</div>
</body>
</html>
```